BRIMLOW Pizza and Wraps

We need a website for a new restaurant called BRIMLOW "PIZZA AND WRAPS".
I have attached fonts, background images, logo, images, content etc.
can provide you with what you need to get the website design done fast and easy

I have uploaded more images of the venue and some menu items. let me know if there is anything I need to provide to make your mission clear and easy

Reason: i would like a little time to provide more feedback to designers

Industry/Entity Type

Restaurant

Coding

Coded - Design and coding required

Number of Pages Required

5+ page

Colors

Designer to choose colors to be used in the design.

Requirements
Must have
• PAGES:
• Our Story
• Menu
• Reservations
• Catering & Delivery
• Contact

```html
<!DOCTYPE html>
<html lang="en">
<head>
<meta charset="utf-8">
<title>BRIMLOW Pizza and Wraps</title>
<link rel="stylesheet" href="https://fonts.googleapis.com/css2?family=Lora:wght@400;700&family=Open+Sans:ital,wght@0,400;0,600;0,700;1,400&display=swap">
<style>
:root{
  --red:#e8232f;
  --red-deep:#c9161f;
  --yellow:#fff200;
  --ink:#1d1d1d;
  --body:#6f6f6f;
  --white:#ffffff;
  --dark:#1a1512;
  --line:#dcdcdc;
}
*{margin:0;padding:0;box-sizing:border-box}
html,body{width:1200px;height:3651px;overflow:hidden;background:var(--white)}
body{font-family:"Open Sans",Arial,sans-serif;color:var(--ink);position:relative}
.abs{position:absolute}
.serif{font-family:"Lora",Georgia,serif}

/* hero */
.hero{left:0;top:0;width:1200px;height:608px;background:radial-gradient(ellipse at 40% 45%,#c9a070 0%,#8a6542 35%,#4a3526 70%,#2a1f18 100%)}
.hero-shade{left:0;top:0;width:1200px;height:608px;background:linear-gradient(rgba(0,0,0,.55),rgba(0,0,0,.15) 30%,rgba(0,0,0,.25))}
.brand{left:97px;top:40px;font-family:"Lora",Georgia,serif;font-weight:700;font-size:46px;color:var(--red);letter-spacing:1px}
.nav{right:97px;top:58px;display:flex;gap:30px;align-items:center;font-family:"Lora",Georgia,serif;font-weight:700;font-size:15px;color:var(--white)}
.nav .active{color:var(--yellow)}
.hero-title{left:0;width:1200px;top:190px;text-align:center;font-family:"Lora",Georgia,serif;font-weight:700;font-size:80px;color:var(--white);letter-spacing:2px}
.hero-sub{left:0;width:1200px;top:290px;text-align:center;font-size:24px;font-weight:600;color:var(--white)}
.btn-ghost{left:501px;top:348px;width:198px;height:49px;border:2px solid var(--white);color:var(--white);font-family:"Lora",Georgia,serif;font-weight:700;font-size:15px;display:flex;align-items:center;justify-content:center}
.dots{display:flex;gap:6px}
.dots span{width:13px;height:13px;border-radius:50%;border:2px solid var(--white)}
.dots span.on{background:var(--white)}
.dots.grey span{border-color:#9a9a9a}
.dots.grey span.on{background:#9a9a9a}

/* cards */
.card{background:var(--white);box-shadow:0 2px 14px rgba(0,0,0,.18)}
.welcome{left:97px;top:555px;width:1003px;height:443px}
.welcome-photo{left:133px;top:51px;width:306px;height:306px;border-radius:50%;border:5px solid var(--red);background:radial-gradient(circle at 45% 45%,#9cc25a,#5d8b32 45%,#b94a38 75%,#3b2b24)}
.welcome h2{left:468px;top:64px;font-family:"Lora",Georgia,serif;font-size:31px;font-weight:700}
.welcome p{left:468px;width:490px;font-size:13px;line-height:24px;color:var(--body)}
.btn-out{border:2px solid #bbb;color:#c9a000;font-family:"Lora",Georgia,serif;font-weight:700;font-size:13px;display:flex;align-items:center;justify-content:center}

.specials{left:0;top:944px;width:1200px;height:511px;background:radial-gradient(ellipse at 50% 50%,#b99a80,#7b5c45 50%,#3f2d22 100%)}
.specials-shade{left:0;top:944px;width:1200px;height:511px;background:rgba(0,0,0,.4)}
.section-title{left:0;width:1200px;text-align:center;font-family:"Lora",Georgia,serif;font-weight:700;font-size:36px}
.btn-yellow{background:var(--yellow);color:var(--ink);font-family:"Lora",Georgia,serif;font-weight:700;font-size:14px;display:flex;align-items:center;justify-content:center}

.menu{left:97px;top:1383px;width:1003px;height:584px}
.dish{border-radius:50%;border:5px solid var(--white);box-shadow:0 0 0 1px #ccc,0 2px 8px rgba(0,0,0,.25)}
.dish-label{font-family:"Lora",Georgia,serif;font-weight:700;font-size:16px;text-align:center;width:200px}

.red-band{left:0;top:1908px;width:1200px;height:716px;background:radial-gradient(ellipse at 50% 55%,#f04a4f,var(--red) 45%,var(--red-deep))}
.feature{width:314px;height:372px;top:2081px;background:var(--white)}
.feature-photo{left:0;top:0;width:314px;height:190px}
.feature-icon{left:123px;top:-34px;width:68px;height:68px;border-radius:50%;background:var(--red);border:3px solid var(--white);display:flex;align-items:center;justify-content:center}
.feature h3{left:0;width:314px;top:220px;text-align:center;font-family:"Lora",Georgia,serif;font-weight:700;font-size:19px}
.feature p{left:30px;width:254px;top:252px;text-align:center;font-size:12px;line-height:19px;color:var(--body)}
.feature .btn-yellow{left:88px;top:353px;width:139px;height:39px;font-size:13px}

.testimonial{left:97px;top:2560px;width:1003px;height:512px}

.contact{left:0;top:3011px;width:1200px;height:640px;background:radial-gradient(ellipse at 50% 40%,#5a3f2c,#2b1f17 55%,var(--dark))}
.contact-shade{left:0;top:3011px;width:1200px;height:640px;background:rgba(0,0,0,.35)}
.label{font-size:12px;font-weight:700;color:var(--white)}
.field{background:var(--white);height:32px}
.info-icon{width:44px;height:44px;border-radius:50%;border:2px solid var(--red);display:flex;align-items:center;justify-content:center}
.info-text{font-size:12px;color:var(--white);line-height:20px}
.hours{left:808px;width:292px;display:flex;justify-content:space-between;font-size:12px;color:var(--white)}
.social{width:28px;height:28px;background:var(--white);border-radius:3px}
</style>
</head>
<body>

<!-- hero -->
<div class="abs hero" role="img" aria-label="Close-up photo of a grilled chicken wrap with garlic sauce and fries"></div>
<div class="abs hero-shade"></div>
<div class="abs brand">BRIMLOW</div>
<nav class="abs nav">
  <span class="active">HOME</span><span>ABOUT</span><span>MENU</span><span>CATERING</span><span>GALLERY</span><span>CONTACT</span>
  <svg width="16" height="16" viewBox="0 0 16 16"><circle cx="6.5" cy="6.5" r="5" fill="none" stroke="#fff" stroke-width="2"/><line x1="10.5" y1="10.5" x2="15" y2="15" stroke="#fff" stroke-width="2.4"/></svg>
</nav>
<h1 class="abs hero-title">PIZZA &amp; WRAPS</h1>
<div class="abs hero-sub">At vero eos et accusamus et iusto odi</div>
<div class="abs btn-ghost">ONLINE ORDERING</div>
<div class="abs dots" style="left:565px;top:512px"><span class="on"></span><span></span><span></span><span></span></div>

<!-- welcome -->
<section class="abs card welcome">
  <div class="abs welcome-photo" role="img" aria-label="Photo of a fresh Greek salad with feta, olives and tomatoes"></div>
  <h2 class="abs">WELCOME TO BRIMLOW</h2>
  <p class="abs" style="top:120px">Nam libero tempore, cum soluta nobis est eligendi optio cumque nihil imp edit quo minus id quod maxime place.</p>
  <p class="abs" style="top:186px">Facere possimus, omnis voluptas assumenda est, omnis dolor remporibus autem quibusdam et aut officiis debitis aut rerum necessitatibus saepe eve niet ut et voluptates repudiandae sint et molestiae non recusanda aqueaar um rerum hic tenetur a sapiente delectus.</p>
  <div class="abs btn-out" style="left:468px;top:333px;width:118px;height:42px">READ MORE</div>
</section>

<!-- daily specials -->
<div class="abs specials" role="img" aria-label="Photo of a plate of hummus topped with shawarma meat"></div>
<div class="abs specials-shade"></div>
<h2 class="abs section-title" style="top:1078px;color:var(--white)">DAILY SPECIALS</h2>
<p class="abs" style="left:250px;width:700px;top:1146px;text-align:center;color:var(--white);font-size:15px;font-weight:600;line-height:30px">Nam libero tempore, cum soluta nobis est eligendi optio cumque nihil impedit quo minus id quod maxime placeat facere possim nis voluptas assumend.</p>
<div class="abs btn-yellow" style="left:482px;top:1236px;width:236px;height:49px">CHECK OUT OUR SPECIALS</div>

<!-- menu -->
<section class="abs card menu">
  <h2 class="abs section-title" style="left:0;width:1003px;top:58px">OUR MENU</h2>
  <div class="abs dish" style="left:27px;top:167px;width:176px;height:176px;background:radial-gradient(#d9c7a8,#9a7e5c)" role="img" aria-label="Photo of a rolled wrap"></div>
  <div class="abs dish" style="left:219px;top:167px;width:176px;height:176px;background:radial-gradient(#d27b3c,#7d3a1c)" role="img" aria-label="Photo of spaghetti with meatballs"></div>
  <div class="abs dish" style="left:385px;top:136px;width:234px;height:234px;background:radial-gradient(#f2d27a,#8a4a2a 60%,#3a2820)" role="img" aria-label="Photo of a breakfast plate with eggs and sausages"></div>
  <div class="abs dish" style="left:611px;top:167px;width:176px;height:176px;background:radial-gradient(#e0c49a,#9c7552)" role="img" aria-label="Photo of a pizza diavola"></div>
  <div class="abs dish" style="left:806px;top:167px;width:176px;height:176px;background:radial-gradient(#e38b45,#a2461f)" role="img" aria-label="Photo of pizza calzones"></div>
  <div class="abs dish-label" style="left:15px;top:367px">Cheese Pizza</div>
  <div class="abs dish-label" style="left:207px;top:367px">Speciality Wraps</div>
  <div class="abs dish-label" style="left:599px;top:367px">Pizza Diavola</div>
  <div class="abs dish-label" style="left:794px;top:367px">Pizza Calzones</div>
  <div class="abs dish-label" style="left:352px;top:413px;width:300px">Wraps &amp; Syrian Pockets</div>
  <p class="abs" style="left:352px;width:300px;top:450px;text-align:center;font-size:12px;line-height:20px;color:var(--body)">Nam libero tempore, cum soluta nobis est eligendi optio cumque nihil impedit quo minus</p>
  <div class="abs dots grey" style="left:468px;top:524px"><span class="on"></span><span></span><span></span><span></span></div>
</section>

<!-- features -->
<div class="abs red-band" role="img" aria-label="Blurred photo of tomatoes in red tones"></div>

<section class="abs feature" style="left:97px">
  <div class="abs feature-photo" style="background:linear-gradient(135deg,#b98a4a,#6a5a3a 55%,#2d2a22)" role="img" aria-label="Photo of iced tea with lemon slices"></div>
  <div class="abs feature-icon"><svg width="28" height="24" viewBox="0 0 28 24"><rect x="2" y="2" width="24" height="20" fill="none" stroke="#fff" stroke-width="2.4"/><path d="M5 19l7-8 5 5 3-3 4 6z" fill="#fff"/><circle cx="19" cy="8" r="2.5" fill="#fff"/></svg></div>
  <h3 class="abs">OUR GALLERY</h3>
  <p class="abs">Nam libero tempore, cum soluta nobis est eligendi optio cumque nihil impedit quo minus id quod maxime placeat facere</p>
  <div class="abs btn-yellow">VIEW MORE</div>
</section>

<section class="abs feature" style="left:443px">
  <div class="abs feature-photo" style="background:linear-gradient(135deg,#8a7560,#c9b49a 50%,#5a4a3a)" role="img" aria-label="Photo of a table set with many dishes"></div>
  <div class="abs feature-icon"><svg width="26" height="26" viewBox="0 0 26 26"><rect x="2" y="4" width="22" height="20" fill="none" stroke="#fff" stroke-width="2.4"/><line x1="2" y1="10" x2="24" y2="10" stroke="#fff" stroke-width="2.4"/><line x1="8" y1="1" x2="8" y2="7" stroke="#fff" stroke-width="2.4"/><line x1="18" y1="1" x2="18" y2="7" stroke="#fff" stroke-width="2.4"/><g fill="#fff"><rect x="6" y="13" width="3" height="3"/><rect x="12" y="13" width="3" height="3"/><rect x="18" y="13" width="3" height="3"/><rect x="6" y="18" width="3" height="3"/><rect x="12" y="18" width="3" height="3"/></g></svg></div>
  <h3 class="abs">MAKE A RESERVATION</h3>
  <p class="abs">Nam libero tempore, cum soluta nobis est eligendi optio cumque nihil impedit quo minus id quod maxime placeat facere</p>
  <div class="abs btn-yellow">BOOK NOW!</div>
</section>

<section class="abs feature" style="left:786px">
  <div class="abs feature-photo" style="background:linear-gradient(135deg,#3a2a20,#b8703a 50%,#d9a060)" role="img" aria-label="Photo of a pizza on a wooden board"></div>
  <div class="abs feature-icon"><svg width="30" height="26" viewBox="0 0 30 26"><ellipse cx="12" cy="10" rx="10" ry="7.5" fill="none" stroke="#fff" stroke-width="2.2"/><path d="M6 16l-2 5 6-3" fill="#fff"/><ellipse cx="19" cy="15" rx="8" ry="6" fill="#fff"/></svg></div>
  <h3 class="abs">BRIMLOW BLOG</h3>
  <p class="abs">Nam libero tempore, cum soluta nobis est eligendi optio cumque nihil impedit quo minus id quod maxime placeat facere</p>
  <div class="abs btn-yellow">VIEW MORE</div>
</section>

<!-- testimonials -->
<section class="abs card testimonial">
  <h2 class="abs section-title" style="left:0;width:1003px;top:52px">CLIENT TESTIMONIALS</h2>
  <svg class="abs" style="left:454px;top:140px" width="96" height="86" viewBox="0 0 96 86"><path d="M4 40C4 18 16 4 38 0v14C26 18 22 26 22 36h18v46H4z" fill="var(--red)"/><path d="M56 40C56 18 68 4 90 0v14C78 18 74 26 74 36h18v46H56z" fill="var(--red)"/></svg>
  <p class="abs" style="left:120px;width:763px;top:253px;text-align:center;font-size:13px;font-style:italic;line-height:26px;color:var(--body)">" Nam libero tempore, cum soluta nobis est eligendi optio cumque nihil impedit quo minus id quod maxime placeat facere possimus, omnis voluptas assumenda est, omnis dolor repellend emporibus autem quibusdam et aut officiis debi tis aut rerum necessitatibus saepe eveniet ut et voluptates repudiandae sint et molestiae "</p>
  <div class="abs" style="left:0;width:1003px;top:364px;text-align:center;font-weight:700;font-size:16px">- Mara Quill</div>
  <div class="abs dots grey" style="left:468px;top:437px"><span class="on"></span><span></span><span></span><span></span></div>
</section>

<!-- contact -->
<div class="abs contact" role="img" aria-label="Dark blurred photo of a pizza"></div>
<div class="abs contact-shade"></div>
<h2 class="abs section-title" style="top:3133px;color:var(--white)">CONTACT US</h2>

<div class="abs label" style="left:97px;top:3200px;font-size:14px">CONTACT FORM</div>
<div class="abs label" style="left:97px;top:3240px;font-weight:400">NAME :</div>
<div class="abs label" style="left:419px;top:3240px;font-weight:400">PHONE NO :</div>
<div class="abs field" style="left:97px;top:3269px;width:312px"></div>
<div class="abs field" style="left:419px;top:3269px;width:309px"></div>
<div class="abs label" style="left:97px;top:3311px;font-weight:400">EMAIL :</div>
<div class="abs field" style="left:97px;top:3335px;width:631px"></div>
<div class="abs label" style="left:97px;top:3376px;font-weight:400">MESSAGE :</div>
<div class="abs field" style="left:97px;top:3403px;width:631px;height:78px"></div>
<div class="abs btn-yellow" style="left:630px;top:3490px;width:98px;height:37px;font-family:'Open Sans',Arial,sans-serif;font-size:13px">SUBMIT</div>

<div class="abs label" style="left:808px;top:3200px;font-size:14px">CONTACT INFORMATION</div>
<div class="abs info-icon" style="left:808px;top:3240px"><svg width="14" height="18" viewBox="0 0 14 18"><path d="M7 0a7 7 0 0 1 7 7c0 5-7 11-7 11S0 12 0 7a7 7 0 0 1 7-7z" fill="var(--red)"/><circle cx="7" cy="7" r="2.5" fill="#2b1f17"/></svg></div>
<div class="abs info-text" style="left:888px;top:3242px">1480 N. Alder Crest Blvd.,<br>Fenwick</div>
<div class="abs info-icon" style="left:808px;top:3293px"><svg width="18" height="13" viewBox="0 0 18 13"><rect width="18" height="13" rx="1" fill="var(--red)"/><path d="M0 1l9 6 9-6" fill="none" stroke="#2b1f17" stroke-width="1.5"/></svg></div>
<div class="abs info-text" style="left:888px;top:3305px">info@brimlow.com</div>
<div class="abs info-icon" style="left:808px;top:3351px"><svg width="16" height="16" viewBox="0 0 16 16"><path d="M3 0l3 4-2 2c1 2 4 5 6 6l2-2 4 3-2 3C7 16 0 9 0 3z" fill="var(--red)"/></svg></div>
<div class="abs info-text" style="left:888px;top:3363px">1 555 014 2290</div>

<div class="abs label" style="left:808px;top:3426px;font-size:14px">OPENING HOURS</div>
<div class="abs hours" style="top:3458px"><span>Monday -</span><span>8 Am - 12 Am</span></div>
<div class="abs hours" style="top:3482px"><span>Tuesday, Wednesday &amp; Thursday</span><span>8 Am - 10 Pm</span></div>
<div class="abs hours" style="top:3509px"><span>Friday &amp; Saturday</span><span>8 Am – Close</span></div>

<div class="abs" style="left:97px;top:3566px;width:1003px;height:1px;background:rgba(255,255,255,.3)"></div>
<div class="abs" style="left:97px;top:3594px;font-size:11px;color:var(--white)">Copyrights © 2017, BRIMLOW . All Rights Reserved.</div>
<div class="abs social" style="left:957px;top:3588px"></div>
<div class="abs social" style="left:995px;top:3588px"></div>
<div class="abs social" style="left:1034px;top:3588px"></div>
<div class="abs social" style="left:1072px;top:3588px"></div>

</body>
</html>
```